creation of business cards for Velmora Sàrl

Velmora S% 26 # 224; rl is a soci% 26 # 233; t% 26 # 233; consultancy that accompanies companies in the development of their business on the market% 26 # 233; Switzerland by providing strategic contacts or market information; and by providing administrative or logistical support. Our consulting skills focus on sectors% 26 # 224; high value added% 26 # 233; e, such as trade in food goods% 26 # 39amp; drinks, fashion% 26amp; lifestyle, products and services for% 26 # 233; s in high-tech industries (pharmaceutical, chemical, m% 26 # 233; pricy 26% 23 #; cision) or sustainable solutions (% 26 # 233; energies renewable, mat% 26 # 233; recyclable materials). As part of the launch of our activity% 26 # 233;, we need% 26 # 39;% 26 # 233; to establish business cards to d% 26 # 233; work our new customers (Swiss or international).

Target Market(s)

Companies wishing to develop their activity% 26 # 233; s in Switzerland or% 26 # 224; l% 26 # 39;% 26 # 233; abroad (mainly in Europe).

Contact Information for Business Card

Prénom NOM
Velmora Sàrl
Bureau de Lavertin
Rue des Tilleuls 14, 2000 Neuchâtel
Tél. : 032 718 46 39
info@velmora-conseil.ch
www.velmora-conseil.ch

Font styles to use
Serif
Sans Serif

Colors

Designer to choose colors to be used in the design.

Requirements
Must have
• The logo The name of the company% 26 # 233; t% 26 # 233; (Velmora S% 26 # 224; rl) One field for the mailing address One field for the number% 26 # 233; ro de t% 26 # 233; l% 26 # 233; phone One field for the % 26 # 39; email address and website

```html
<!DOCTYPE html>
<html lang="fr">
<head>
<meta charset="utf-8">
<title>Velmora Sàrl – cartes de visite</title>
<link rel="stylesheet" href="https://fonts.googleapis.com/css2?family=Roboto:wght@300;400;700&display=swap">
<style>
  :root {
    --teal: #053f58;
    --teal-dark: #032d40;
    --paper: #ffffff;
    --muted: #a9b6bf;
    --backdrop: #e9e7e4;
  }
  * { box-sizing: border-box; margin: 0; padding: 0; }
  html, body {
    width: 1200px; height: 716px; overflow: hidden;
    background: var(--backdrop);
    font-family: "Roboto", Arial, sans-serif;
  }
  .sheet {
    width: 1200px; height: 716px;
    display: flex; align-items: center; justify-content: center; gap: 44px;
  }
  .card {
    position: relative;
    width: 520px; height: 320px;
    box-shadow: 0 10px 28px rgba(0,0,0,.18);
    overflow: hidden;
  }

  /* Front */
  .card--front { background: var(--teal); }
  .front-wordmark {
    position: absolute; right: 46px; bottom: 48px;
    color: var(--paper);
    font-weight: 300; font-size: 46px; letter-spacing: 9px;
  }

  /* Back */
  .card--back { background: var(--paper); color: var(--teal); }
  .brand {
    position: absolute; left: 64px; top: 58px;
    display: flex; align-items: center; gap: 22px;
  }
  .brand-square {
    width: 52px; height: 52px; border-radius: 10px; background: var(--teal);
  }
  .brand-name {
    font-weight: 300; font-size: 44px; letter-spacing: 8px; color: var(--teal);
  }
  .details {
    position: absolute; left: 0; right: 0; top: 170px;
    display: flex; justify-content: center; align-items: stretch; gap: 18px;
  }
  .identity { text-align: right; padding-top: 4px; }
  .identity-name { font-weight: 700; font-size: 19px; }
  .identity-company { font-weight: 300; font-size: 14px; color: var(--muted); margin-top: 2px; }
  .divider { width: 1px; background: var(--teal); }
  .contact-list { list-style: none; font-size: 13.5px; line-height: 1.55; }
  .contact-list li { display: flex; align-items: center; gap: 8px; }
  .contact-icon { width: 11px; height: 11px; fill: var(--muted); flex: none; }
  .contact-web-host { color: var(--muted); }
  .address {
    position: absolute; left: 0; right: 0; bottom: 34px;
    text-align: center; font-size: 14px; font-weight: 400;
  }
</style>
</head>
<body>
<main class="sheet">
  <section class="card card--front" aria-label="Recto de la carte">
    <div class="front-wordmark">VELMORA</div>
  </section>

  <section class="card card--back" aria-label="Verso de la carte">
    <div class="brand">
      <span class="brand-square" aria-hidden="true"></span>
      <span class="brand-name">VELMORA</span>
    </div>

    <div class="details">
      <div class="identity">
        <p class="identity-name">Prénom NOM</p>
        <p class="identity-company">Velmora Sàrl</p>
      </div>
      <span class="divider" aria-hidden="true"></span>
      <ul class="contact-list">
        <li>
          <svg class="contact-icon" viewBox="0 0 24 24" aria-hidden="true"><path d="M6.6 10.8a15 15 0 0 0 6.6 6.6l2.2-2.2c.3-.3.7-.4 1-.2 1.1.4 2.3.6 3.6.6.6 0 1 .4 1 1V20c0 .6-.4 1-1 1A17 17 0 0 1 3 4c0-.6.4-1 1-1h3.5c.6 0 1 .4 1 1 0 1.3.2 2.5.6 3.6.1.3 0 .7-.2 1z"/></svg>
          <span>Tél. : 032 718 46 39</span>
        </li>
        <li>
          <svg class="contact-icon" viewBox="0 0 24 24" aria-hidden="true"><path d="M2 5h20v14H2zm2 2v.5l8 5 8-5V7zm0 3v7h16v-7l-8 5z"/></svg>
          <span>info@velmora-conseil.ch</span>
        </li>
        <li>
          <svg class="contact-icon" viewBox="0 0 24 24" aria-hidden="true"><path d="M12 2a10 10 0 1 0 0 20 10 10 0 0 0 0-20zm6.9 9h-3a15 15 0 0 0-1.3-5.5A8 8 0 0 1 18.9 11zM12 4.1c.9 1.2 1.7 3.6 1.9 6.9h-3.8c.2-3.3 1-5.7 1.9-6.9zM9.4 5.5A15 15 0 0 0 8.1 11h-3a8 8 0 0 1 4.3-5.5zM5.1 13h3a15 15 0 0 0 1.3 5.5A8 8 0 0 1 5.1 13zm6.9 6.9c-.9-1.2-1.7-3.6-1.9-6.9h3.8c-.2 3.3-1 5.7-1.9 6.9zm2.6-1.4a15 15 0 0 0 1.3-5.5h3a8 8 0 0 1-4.3 5.5z"/></svg>
          <span>www.<span class="contact-web-host">velmora-conseil.ch</span></span>
        </li>
      </ul>
    </div>

    <p class="address">Bureau de Lavertin, Rue des Tilleuls 14, 2000 Neuchâtel</p>
  </section>
</main>
</body>
</html>
```